Rambler Zinfandel wine label

I need a wine label designed for a new wine brand. I am open to anything, but I think the simpler and bolder the better so it will stand out on the shelf amongst the hundreds of brands out there.
Label should have the word RAMBLER buy itself with the word Zinfandel under it.

```html
<!DOCTYPE html>
<html lang="en">
<head>
<meta charset="utf-8">
<title>Rambler Zinfandel – Wine Label</title>
<link rel="stylesheet" href="https://fonts.googleapis.com/css2?family=Cousine&family=Open+Sans:wght@700&display=swap">
<style>
  :root {
    --label-bg: #ffffff;
    --band-magenta: #d010dc;
    --text-white: #ffffff;
  }
  html, body {
    margin: 0;
    padding: 0;
    overflow: hidden;
    background: var(--label-bg);
  }
  .label {
    position: relative;
    width: 1200px;
    height: 720px;
    overflow: hidden;
    background: var(--label-bg);
  }
  .label__band {
    position: absolute;
    left: 0;
    top: 0;
    width: 1200px;
    height: 720px;
  }
  .label__band path {
    fill: var(--band-magenta);
  }
  .label__brand {
    position: absolute;
    left: 152px;
    top: 338px;
    margin: 0;
    font-family: "Cousine", "Courier New", monospace;
    font-weight: 400;
    font-size: 166px;
    line-height: 1;
    letter-spacing: 0;
    color: var(--text-white);
  }
  .label__varietal {
    position: absolute;
    left: 1020px;
    top: 435px;
    margin: 0;
    transform: translate(-50%, -50%) rotate(90deg);
    font-family: "Open Sans", Arial, sans-serif;
    font-weight: 700;
    font-size: 30px;
    line-height: 1;
    white-space: nowrap;
    color: var(--text-white);
  }
</style>
</head>
<body>
  <main class="label">
    <svg class="label__band" viewBox="0 0 1200 720" aria-hidden="true">
      <path d="M0,218
        q15,-6 30,0 t30,0 t30,0 t30,0 t30,0 t30,0 t30,0 t30,0 t30,0 t30,0
        t30,0 t30,0 t30,0 t30,0 t30,0 t30,0 t30,0 t30,0 t30,0 t30,0
        t30,0 t30,0 t30,0 t30,0 t30,0 t30,0 t30,0 t30,0 t30,0 t30,0
        t30,0 t30,0 t30,0 t30,0 t30,0 t30,0 t30,0 t30,0 t30,0 t30,0
        L1200,626
        q-15,6 -30,0 t-30,0 t-30,0 t-30,0 t-30,0 t-30,0 t-30,0 t-30,0 t-30,0 t-30,0
        t-30,0 t-30,0 t-30,0 t-30,0 t-30,0 t-30,0 t-30,0 t-30,0 t-30,0 t-30,0
        t-30,0 t-30,0 t-30,0 t-30,0 t-30,0 t-30,0 t-30,0 t-30,0 t-30,0 t-30,0
        t-30,0 t-30,0 t-30,0 t-30,0 t-30,0 t-30,0 t-30,0 t-30,0 t-30,0 t-30,0
        Z"/>
    </svg>
    <h1 class="label__brand">RAMBLER</h1>
    <p class="label__varietal">Zinfandel</p>
  </main>
</body>
</html>
```